Rural contractor needs professional informative business card

We need a business card design that looks professional but also includes information about the services that the business offers.
The business is an earthmoving and transport business. All of the services offered are listed on the old card attached.
The business is aimed at farmers so the design we are after is a classic look. The card needs to include all of the information that is listed on the old card design uploaded as an attachment. We recognize that this is a lot of information to fit on a business card but it also operates as a key marketing tool so is very important to the business.
Feel free to send me your questions.
Thanks
Reason: We are having trouble deciding between all these great designs - thank you for your efforts
We would love to see some designs using red with a little white and black. Also feel free to re-design our logo if you feel it needs to be to fit your designs. Thank you

```html
<!DOCTYPE html>
<html lang="en">
<head>
<meta charset="utf-8">
<title>RB Hallard Contracting – Business Card</title>
<link href="https://fonts.googleapis.com/css2?family=Montserrat:wght@400;500;600&display=swap" rel="stylesheet">
<style>
  :root{
    --backdrop:#8f8f8f;
    --paper:#ffffff;
    --ink:#3c3c3c;
    --logo-grey:#9a9a9a;
    --brand-red:#e4202a;
    --card-black:#0b0b0b;
    --stripe:#3a2220;
    --white:#ffffff;
  }
  *{box-sizing:border-box;margin:0;padding:0}
  html,body{width:1200px;height:640px;overflow:hidden}
  body{background:var(--backdrop);font-family:"Montserrat",Arial,sans-serif;position:relative}

  .card{position:absolute;width:520px;height:300px;overflow:hidden;box-shadow:0 6px 14px rgba(0,0,0,.35)}

  /* Front */
  .card-front{left:50px;top:50px;background:var(--paper)}
  .brand{position:absolute;left:36px;top:30px;display:flex;align-items:center;gap:12px}
  .brand-mark{width:14px;height:14px;background:var(--logo-grey)}
  .brand-name{font-weight:600;font-size:26px;line-height:1.05;color:var(--logo-grey);letter-spacing:.5px}
  .holder{position:absolute;right:34px;top:100px;text-align:right}
  .holder-name{font-weight:500;font-size:20px;color:var(--brand-red)}
  .tagline{position:absolute;left:40px;right:34px;top:134px;display:flex;align-items:center;gap:6px}
  .tagline-rule{flex:1;height:1px;background:var(--ink)}
  .tagline-text{font-size:12px;font-weight:500;color:var(--ink);letter-spacing:.3px}
  .contacts{position:absolute;left:40px;top:172px;list-style:none}
  .contacts li{display:flex;align-items:center;gap:10px;height:24px;font-size:13.5px;color:var(--ink)}
  .contacts svg{width:18px;height:18px;flex:none}
  .band-red{position:absolute;left:0;bottom:0;width:330px;height:26px;background:var(--brand-red)}
  .band-black{position:absolute;right:0;bottom:0;width:196px;height:40px;background:var(--card-black);border-top-left-radius:10px}

  /* Back */
  .card-back{left:630px;top:290px;background:var(--card-black)}
  .back-brand{position:absolute;left:0;right:0;top:50px;display:flex;justify-content:center;align-items:center;gap:14px}
  .back-brand .brand-mark{width:18px;height:18px;background:var(--brand-red)}
  .back-brand .brand-name{font-size:30px;color:var(--brand-red)}
  .services{position:absolute;left:0;right:0;top:172px}
  .row{height:21px;display:flex;align-items:center}
  .row.striped{background:var(--stripe)}
  .col{font-size:13px;color:var(--white);display:flex;align-items:center;gap:6px}
  .col-a{width:300px;padding-left:90px}
  .col-b{padding-left:2px}
  .heading{color:var(--brand-red);font-weight:600;font-size:12.5px}
  .bullet{width:7px;height:7px;background:var(--brand-red);flex:none}
</style>
</head>
<body>

<section class="card card-front" aria-label="Business card front">
  <div class="brand">
    <span class="brand-mark"></span>
    <span class="brand-name">RB Hallard<br>Contracting</span>
  </div>
  <div class="holder"><p class="holder-name">Rowan Hallard</p></div>
  <div class="tagline">
    <span class="tagline-rule"></span>
    <span class="tagline-text">EARTHMOVING &amp; TRANSPORT SOLUTIONS</span>
  </div>
  <ul class="contacts">
    <li>
      <svg viewBox="0 0 20 20" aria-hidden="true"><circle cx="10" cy="10" r="10" fill="#e4202a"/><path d="M7 5.5l2 2-1.2 1.4c.7 1.4 1.8 2.5 3.3 3.3l1.4-1.2 2 2-1.3 1.6C10 14.4 5.6 10 5.4 6.8z" fill="#fff"/></svg>
      <span>0400 123 987</span>
    </li>
    <li>
      <svg viewBox="0 0 20 20" aria-hidden="true"><circle cx="10" cy="10" r="10" fill="#e4202a"/><rect x="5" y="6.5" width="10" height="7" fill="none" stroke="#fff" stroke-width="1.2"/><path d="M5 6.8l5 4 5-4" fill="none" stroke="#fff" stroke-width="1.2"/></svg>
      <span>rowan@hallardcontracting.com</span>
    </li>
    <li>
      <svg viewBox="0 0 20 20" aria-hidden="true"><circle cx="10" cy="10" r="10" fill="#e4202a"/><g fill="none" stroke="#fff" stroke-width="1"><circle cx="10" cy="10" r="5"/><ellipse cx="10" cy="10" rx="2.2" ry="5"/><path d="M5 10h10"/></g></svg>
      <span>www.hallardcontracting.com</span>
    </li>
    <li>
      <svg viewBox="0 0 20 20" aria-hidden="true"><circle cx="10" cy="10" r="10" fill="#e4202a"/><path d="M10 4.5a3.6 3.6 0 0 0-3.6 3.6c0 2.7 3.6 7 3.6 7s3.6-4.3 3.6-7A3.6 3.6 0 0 0 10 4.5z" fill="#fff"/><circle cx="10" cy="8.1" r="1.3" fill="#e4202a"/></svg>
      <span>52 Wattle Road, Dunmore 2880</span>
    </li>
  </ul>
  <div class="band-red"></div>
  <div class="band-black"></div>
</section>

<section class="card card-back" aria-label="Business card back">
  <div class="back-brand">
    <span class="brand-mark"></span>
    <span class="brand-name">RB Hallard Contracting</span>
  </div>
  <div class="services">
    <div class="row striped">
      <span class="col col-a heading">Earthmoving</span>
      <span class="col col-b heading">Transport</span>
    </div>
    <div class="row">
      <span class="col col-a"><i class="bullet"></i>Road Building &amp; Maintenance</span>
      <span class="col col-b"><i class="bullet"></i>Grain</span>
    </div>
    <div class="row striped">
      <span class="col col-a"><i class="bullet"></i>Poly Pipe Laying</span>
      <span class="col col-b"><i class="bullet"></i>Cotton</span>
    </div>
    <div class="row">
      <span class="col col-a"><i class="bullet"></i>Clearing fence lines</span>
      <span class="col col-b"><i class="bullet"></i>Sand &amp; Gravel</span>
    </div>
    <div class="row striped">
      <span class="col col-a"><i class="bullet"></i>Sand &amp; Gravel Supplies</span>
      <span class="col col-b"><i class="bullet"></i>Wool</span>
    </div>
  </div>
</section>

</body>
</html>
```